Brindle Structures Construction Company Seeking Modern Website

We are a small construction company wanting to create a web presence. We don't have much in the way of current content but will get photos as they come in. Attached is a picture of our business card.
The pages we would like on the menu are:
Home
Portfolio
Product Specs
Testimonials
Our Process
Contact
Some designs we like are:
http://www.tovenquarnsheds.example/
http://www.qzrsheds.example/
http://pannowsheds.example/
http://wistenhalls.example/
Not much requirements other than that so feel free to be creative!
Updates
Target Market(s)
Construction
Commercial and Residential Buildings
Industry/Entity Type
Construction Company
Number of Pages Required
5+ page
Look and feel

```html
<!DOCTYPE html>
<html lang="en">
<head>
<meta charset="utf-8">
<title>Brindle Structures</title>
<link href="https://fonts.googleapis.com/css2?family=Arimo:wght@400;700&family=Open+Sans:ital,wght@0,400;0,600;1,400&display=swap" rel="stylesheet">
<style>
:root{
  --blue:#1aa3dc;
  --red:#d8262c;
  --ink:#2b2b2b;
  --text:#555;
  --muted:#777;
  --band:#dfe5ea;
  --footer:#3b3b3b;
  --footer-line:#4a4a4a;
  --footer-text:#d8d8d8;
}
*{margin:0;padding:0;box-sizing:border-box}
html,body{width:1200px;height:2222px;overflow:hidden;background:#fff}
body{position:relative;font-family:"Open Sans",Arial,sans-serif;color:var(--text)}
.abs{position:absolute}
.heading{font-family:"Arimo",Arial,sans-serif;font-weight:700;color:var(--ink)}
.accent{color:var(--blue)}

.topbar{left:0;top:0;width:1200px;height:36px;background:var(--blue);color:#fff;font-family:"Arimo",Arial,sans-serif;font-size:13px}
.topbar-links{left:98px;top:10px;display:flex;gap:28px}
.topbar-links span{display:flex;align-items:center;gap:7px}
.topbar-call{right:101px;top:10px;font-weight:700;display:flex;align-items:center;gap:8px}
.icon{width:12px;height:12px;fill:currentColor}

.header{left:0;top:36px;width:1200px;height:79px;background:#fff}
.brand{left:76px;top:78px;height:66px;width:282px;display:flex;align-items:center;justify-content:center;gap:10px;background:#fff;border-radius:34px;z-index:3;font-family:"Arimo",Arial,sans-serif;font-weight:700;font-size:26px;color:var(--blue)}
.brand-dot{width:14px;height:14px;border-radius:50%;background:var(--red);flex:none}
.nav{right:68px;top:68px;display:flex;gap:32px;font-family:"Arimo",Arial,sans-serif;font-size:15px;color:#444}
.nav span{display:flex;align-items:center;gap:7px}
.nav .current{color:var(--red)}

.hero{left:0;top:115px;width:1200px;height:441px;background:linear-gradient(180deg,#9fc1dc 0%,#c9dbe8 30%,#8d8276 48%,#a7a39c 62%,#d3d4d2 100%)}
.hero-title{left:0;top:298px;width:1200px;text-align:center;font-family:"Arimo",Arial,sans-serif;font-weight:700;font-size:78px;line-height:90px;color:rgba(255,255,255,.55)}
.dots{display:flex;gap:4px}
.dots i{width:10px;height:10px;border-radius:50%;border:1.5px solid #fff;display:block}
.dots i.on{background:var(--red);border-color:var(--red)}
.hero-dots{left:573px;top:521px}

.welcome-title{left:0;top:595px;width:1200px;text-align:center;font-size:20px}
.welcome-copy{left:200px;top:636px;width:800px;text-align:center;font-size:12px;line-height:22px}

.photo-frame{border:1px solid #ddd;padding:4px;background:#fff;box-shadow:0 1px 3px rgba(0,0,0,.08)}
.photo{width:100%;height:100%}
.feature-title{font-size:15px;text-align:center}
.feature-copy{font-size:12px;line-height:21px;text-align:center}
.feature-copy p{margin-bottom:12px}
.read-more{color:var(--red);font-size:13px;font-weight:600;text-align:center}

.band{left:0;top:1267px;width:1200px;height:299px;background:linear-gradient(180deg,#e4e9ed,#d6dde3)}
.band-title{left:0;top:1298px;width:1200px;text-align:center;font-size:20px}
.quote{left:185px;top:1340px;width:830px;text-align:center;font-style:italic;font-size:12px;line-height:24px;color:#666}
.qmark{color:var(--red);font-family:Georgia,serif;font-weight:700;font-size:22px;font-style:normal;vertical-align:-4px;margin:0 8px}
.avatar{left:504px;top:1422px;width:80px;height:80px;border-radius:50%;border:4px solid #fff;background:linear-gradient(180deg,#d9cbbd,#b59883);box-shadow:0 1px 3px rgba(0,0,0,.2)}
.client-name{left:597px;top:1452px;font-weight:600;font-size:12px;color:#333}
.band-dots{left:579px;top:1525px}
.band-dots i{border-color:#bbb;background:#fff}

.portfolio-title{left:0;top:1600px;width:1200px;text-align:center;font-size:20px;display:flex;justify-content:center;align-items:center;gap:26px}
.chev{width:14px;height:20px;fill:none;stroke:#999;stroke-width:2.5}
.work{width:175px}
.work .photo-frame{height:141px}
.work-label{font-family:"Arimo",Arial,sans-serif;font-size:14px;color:#333;text-align:center;text-transform:uppercase}
.work-sub{font-style:italic;font-size:12px;color:var(--blue);text-align:center}

.footer{left:0;top:1914px;width:1200px;height:308px;background:var(--footer)}
.footer-brand{left:108px;top:2031px;font-family:"Arimo",Arial,sans-serif;font-weight:700;font-size:20px;line-height:30px;color:var(--blue);display:flex;align-items:center;gap:9px;white-space:nowrap}
.footer-brand .brand-dot{width:12px;height:12px}
.footer-col{top:1948px;color:var(--footer-text)}
.footer-col h4{font-family:"Arimo",Arial,sans-serif;font-size:15px;color:#fff;font-weight:700;margin-bottom:18px;white-space:nowrap}
.footer-col li{list-style:none;font-size:12px;line-height:25px}
.contact-row{display:flex;gap:14px;font-size:12px;line-height:16px;margin-bottom:18px}
.contact-row svg{flex:none;width:16px;height:16px;fill:#fff}
.socials{display:flex;gap:10px}
.socials i{width:20px;height:20px;background:#fff;border-radius:3px;display:block}
.footer-rule{left:98px;top:2158px;width:1004px;height:1px;background:var(--footer-line)}
.copyright{left:98px;top:2180px;font-size:12px;color:var(--footer-text)}
.legal{right:99px;top:2180px;font-size:12px;color:var(--footer-text)}
</style>
</head>
<body>

<div class="abs topbar">
  <div class="abs topbar-links">
    <span><svg class="icon" viewBox="0 0 12 12"><circle cx="6" cy="6" r="6"/></svg>FAQ</span>
    <span><svg class="icon" viewBox="0 0 12 12"><rect x="0" y="3" width="12" height="8" rx="1"/><rect x="4" y="1" width="4" height="3" fill="none" stroke="#fff"/></svg>Careers</span>
    <span><svg class="icon" viewBox="0 0 12 12"><path d="M1 5h3v7H1zM5 5l3-5c1 0 2 1 1 3h3v3l-2 6H5z"/></svg>Support</span>
  </div>
  <div class="abs topbar-call"><svg class="icon" viewBox="0 0 12 12"><path d="M2 0l3 3-1.5 1.5a7 7 0 0 0 4 4L9 7l3 3-2 2C5 12 0 7 0 2z"/></svg>CALL US TODAY! &nbsp;1 888 888 8888</div>
</div>

<div class="abs header"></div>
<div class="abs brand"><span class="brand-dot"></span>Brindle Structures</div>
<nav class="abs nav">
  <span class="current"><svg class="icon" viewBox="0 0 12 12"><path d="M6 0l6 6h-2v6H7V8H5v4H2V6H0z"/></svg>Home</span>
  <span><svg class="icon" viewBox="0 0 12 12"><rect x="0" y="1" width="12" height="10" fill="none" stroke="currentColor" stroke-width="1.5"/><path d="M2 9l3-4 2 2 1-1 2 3z"/></svg>Portfolio</span>
  <span><svg class="icon" viewBox="0 0 12 12"><path d="M6 0l6 6h-2v6H2V6H0z"/></svg>Product Specs</span>
  <span><svg class="icon" viewBox="0 0 12 12"><ellipse cx="6" cy="5" rx="6" ry="4.5"/><path d="M2 8l-1 4 4-3z"/></svg>Testimonials</span>
  <span><svg class="icon" viewBox="0 0 12 12"><circle cx="6" cy="6" r="4" fill="none" stroke="currentColor" stroke-width="3" stroke-dasharray="2 1.2"/></svg>Our Process</span>
  <span><svg class="icon" viewBox="0 0 12 12"><path d="M2 0l3 3-1.5 1.5a7 7 0 0 0 4 4L9 7l3 3-2 2C5 12 0 7 0 2z"/></svg>Contact</span>
  <span><svg class="icon" viewBox="0 0 12 12"><circle cx="5" cy="5" r="3.8" fill="none" stroke="currentColor" stroke-width="1.8"/><path d="M8 8l3.5 3.5" stroke="currentColor" stroke-width="2"/></svg></span>
</nav>

<div class="abs hero" role="img" aria-label="Photo of new brick homes with tiled roofs beside a freshly poured concrete slab under a blue sky"></div>
<div class="abs hero-title">Brindle Structures</div>
<div class="abs dots hero-dots"><i class="on"></i><i></i><i></i><i></i></div>

<h1 class="abs heading welcome-title">WELCOME TO <span class="accent">BRINDLE STRUCTURES</span></h1>
<p class="abs welcome-copy">Sed ut perspiciatis unde omnis iste natus error sit voluptatem accusantium doloremque laudantium, totam rem aperiam, eaque ipsa quae ab inventore veritatis et quasi architecto beatae vitae dicta sunt explicabo. Nemo enim ipsam voluptatem quia voluptas sit aspernatur aut odit aut fugit, sed quia consequuntur magni dolores eos qui ratione voluptatem sequi nesciunt.</p>

<div class="abs photo-frame" style="left:98px;top:741px;width:483px;height:281px">
  <div class="photo" role="img" aria-label="Photo of a two-storey rendered house under construction with bricks stacked in front" style="background:linear-gradient(180deg,#3f7fc7 0%,#8fb5de 35%,#e6e1d8 55%,#b79c82 100%)"></div>
</div>
<h2 class="abs heading feature-title" style="left:98px;top:1044px;width:483px">RESIDENTIAL CONSTRUCTION</h2>
<div class="abs feature-copy" style="left:98px;top:1076px;width:483px">
  <p>At vero eos et accusamus et iusto odio dignissimos ducimus qui blanditiis praesem vol atum deleniti atque corrupti quos dolores et qua.</p>
  <p>Molestias excepturi sint ditate nonp vident, similique sunt in culpa qui officia deserunt mollitia animi, id est laborum et dol orum fuuidem rerum facilis est quas molestias excepturi sint ditate nonp vident..</p>
</div>
<div class="abs read-more" style="left:98px;top:1209px;width:483px">Read More &gt;&gt;</div>

<h2 class="abs heading feature-title" style="left:616px;top:736px;width:485px">COMMERCIAL CONSTRUCTION</h2>
<div class="abs feature-copy" style="left:616px;top:768px;width:485px">
  <p>At vero eos et accusamus et iusto odio dignissimos ducimus qui blanditiis praesem vol atum deleniti atque corrupti quos dolores et qua.</p>
  <p>Molestias excepturi sint ditate nonp vident, similique sunt in culpa qui officia deserunt mollitia animi, id est laborum et dol orum fuuidem rerum facilis est quas molestias excepturi sint ditate nonp vident..</p>
</div>
<div class="abs read-more" style="left:616px;top:901px;width:485px">Read More &gt;&gt;</div>
<div class="abs photo-frame" style="left:616px;top:944px;width:485px;height:280px">
  <div class="photo" role="img" aria-label="Photo of a multi-storey timber-framed building wrapped in scaffolding" style="background:linear-gradient(180deg,#4a86d0 0%,#9ec0e6 30%,#c8a27c 55%,#8e6a4c 100%)"></div>
</div>

<div class="abs band" role="img" aria-label="Faint background photo of a building facade"></div>
<h2 class="abs heading band-title">CLIENT <span class="accent">TESTIMONIALS</span></h2>
<p class="abs quote"><span class="qmark">&ldquo;</span>On the other hand, we denounce with righteous indignation and dislike men who are so beguiled and demoralized by the charms of pleasure of the moment, so blinded by desire, that they cannot foresee the pain and trouble that are bound to ensue;nd equal blame belongs to those who fail in their duty through weakness of will, which is the same as saying through shrinking from toil and pain.<span class="qmark">&rdquo;</span></p>
<div class="abs avatar" role="img" aria-label="Portrait photo of the client"></div>
<div class="abs client-name">- MARLO VENNING</div>
<div class="abs dots band-dots"><i class="on" style="background:var(--red);border-color:var(--red)"></i><i></i><i></i></div>

<h2 class="abs heading portfolio-title">
  <svg class="chev" viewBox="0 0 14 20"><path d="M11 2L3 10l8 8"/></svg>
  <span>OUR <span class="accent">PORTFOLIO</span></span>
  <svg class="chev" viewBox="0 0 14 20"><path d="M3 2l8 8-8 8"/></svg>
</h2>

<div class="abs work" style="left:98px;top:1667px">
  <div class="photo-frame"><div class="photo" role="img" aria-label="Photo of a timber-framed house" style="background:linear-gradient(180deg,#5b8fcf,#b7c9d8 45%,#a58d70)"></div></div>
  <div class="work-label" style="margin-top:14px">Residential</div>
  <div class="work-sub">( Home )</div>
</div>
<div class="abs work" style="left:305px;top:1663px">
  <div class="work-label">Commercial</div>
  <div class="work-sub">( School )</div>
  <div class="photo-frame" style="margin-top:12px"><div class="photo" role="img" aria-label="Photo of a red brick school building" style="background:linear-gradient(180deg,#4d86d4,#a9c3e0 35%,#8f5a44 60%,#6f7a5a)"></div></div>
</div>
<div class="abs work" style="left:513px;top:1667px">
  <div class="photo-frame"><div class="photo" role="img" aria-label="Photo of an apartment block under construction" style="background:linear-gradient(180deg,#6b9ad6,#c1b39b 50%,#8c7a66)"></div></div>
  <div class="work-label" style="margin-top:14px">Residential</div>
  <div class="work-sub">( Apartments )</div>
</div>
<div class="abs work" style="left:719px;top:1663px">
  <div class="work-label">Commercial</div>
  <div class="work-sub">( Office )</div>
  <div class="photo-frame" style="margin-top:12px"><div class="photo" role="img" aria-label="Photo of a modern office building" style="background:linear-gradient(180deg,#4f8ad6,#a7c2e3 35%,#b08d63 60%,#6e6e5c)"></div></div>
</div>
<div class="abs work" style="left:924px;top:1667px">
  <div class="photo-frame"><div class="photo" role="img" aria-label="Photo of a hospital entrance" style="background:linear-gradient(180deg,#a9c4e0,#d9d9d9 45%,#8e959b)"></div></div>
  <div class="work-label" style="margin-top:14px">Commercial</div>
  <div class="work-sub">( Hospital )</div>
</div>

<footer class="abs footer"></footer>
<div class="abs footer-brand"><span class="brand-dot"></span>Brindle Structures</div>
<div class="abs footer-col" style="left:344px">
  <h4>Information</h4>
  <ul><li>Home</li><li>Portfolio</li><li>Product Specs</li><li>Testimonials</li><li>Our Process</li><li>Contact</li></ul>
</div>
<div class="abs footer-col" style="left:494px">
  <h4>Why Brindle Structures</h4>
  <ul><li>Our Value</li><li>Our Products</li><li>Our Process</li><li>Our Pricing</li><li>Our Staff</li><li>Our Construction</li></ul>
</div>
<div class="abs footer-col" style="left:690px">
  <h4>Quick Links</h4>
  <ul><li>FAQ</li><li>Help</li><li>Newsletter</li><li>Office Locator</li><li>Contact Us</li><li>Careers</li></ul>
</div>
<div class="abs footer-col" style="left:837px;width:270px">
  <h4>Contact Us</h4>
  <div class="contact-row"><svg viewBox="0 0 16 16"><path d="M8 0a5 5 0 0 1 5 5c0 4-5 11-5 11S3 9 3 5a5 5 0 0 1 5-5zm0 3a2 2 0 1 0 0 4 2 2 0 0 0 0-4z"/></svg><span>At vero eos et accusamus et iusto odio dig ducimus qui blanditiis praesen</span></div>
  <div class="contact-row"><svg viewBox="0 0 16 16"><path d="M3 0l4 4-2 2a9 9 0 0 0 5 5l2-2 4 4-3 3C6 16 0 10 0 3z"/></svg><span>(000) 1 888 888 8888 &nbsp; | &nbsp; 1 222 222 2222</span></div>
  <div class="contact-row"><svg viewBox="0 0 16 16"><rect x="0" y="2" width="16" height="12" rx="1"/><path d="M1 3l7 6 7-6" fill="none" stroke="#3b3b3b" stroke-width="1.5"/></svg><span style="text-decoration:underline">info@brindlestructures.example</span></div>
  <div class="socials"><i></i><i></i><i></i><i></i></div>
</div>
<div class="abs footer-rule"></div>
<div class="abs copyright">Copyrights &copy; 2015, Brindle Structures, Inc. All Rights Reserved.</div>
<div class="abs legal">Terms &amp; Conditions &nbsp;| &nbsp;Privacy Policy &nbsp;| &nbsp;Site Map</div>

</body>
</html>
```